Personal Injury Book Ad Photo Set

I need a series of images for a Pagebloom ad campaign for promoting a book titled "Making Sense of an Accident Claim".

```html
<!DOCTYPE html>
<html lang="en">
<head>
<meta charset="utf-8">
<title>Making Sense of an Accident Claim – Book Ad</title>
<link href="https://fonts.googleapis.com/css2?family=Anton&family=Alfa+Slab+One&family=Libre+Baskerville:wght@700&display=swap" rel="stylesheet">
<style>
  :root {
    --page: #ffffff;
    --ink-dark: #0b0d12;
    --ink-deep: #141a24;
    --navy: #0f2557;
    --royal: #0e4fb0;
    --sky: #3cc0ee;
    --steel: #6b7787;
    --white: #ffffff;
    --yellow: #f6e927;
    --photo-warm: #c9a27a;
    --photo-shadow: #2a2420;
  }
  * { box-sizing: border-box; margin: 0; padding: 0; }
  html, body { width: 1200px; height: 1000px; overflow: hidden; background: var(--page); }

  .ad {
    position: absolute; left: 158px; top: 83px; width: 860px; height: 832px;
    overflow: hidden;
    background: radial-gradient(ellipse at 60% 25%, #2a2d33 0%, var(--ink-deep) 45%, var(--ink-dark) 100%);
    box-shadow: -6px 6px 10px rgba(0,0,0,0.35);
  }
  .ad__backdrop { position: absolute; inset: 0 0 420px 0;
    background: linear-gradient(160deg, #1c1e22 0%, #2f2b28 45%, #121418 100%); opacity: .8; }
  .ad__shapes { position: absolute; inset: 0; }

  .headline { position: absolute; left: 0; right: 0; top: 62px; text-align: center;
    font-family: "Anton", "Impact", sans-serif; text-transform: uppercase; line-height: 1; }
  .headline__top { color: var(--sky); font-size: 80px; letter-spacing: 1px; }
  .headline__bottom { display: block; margin-top: 8px; color: var(--white); font-size: 84px; letter-spacing: 1px;
    -webkit-text-stroke: 14px var(--navy); paint-order: stroke fill; }

  .book { position: absolute; background: var(--ink-dark); overflow: hidden; text-align: center;
    box-shadow: 0 8px 18px rgba(0,0,0,.6); }
  .book--side { top: 347px; width: 170px; height: 295px; }
  .book--left { left: 230px; }
  .book--right { left: 535px; }
  .book--main { left: 339px; top: 250px; width: 245px; height: 432px; z-index: 2; border-right: 6px solid #c8ccd2; }
  .book__photo { width: 100%; height: 55%;
    background: linear-gradient(160deg, #efe6d8 0%, var(--photo-warm) 35%, #5b4a3e 70%, var(--photo-shadow) 100%); }
  .book__title { font-family: "Libre Baskerville", Georgia, serif; color: var(--white); line-height: 1; }
  .book--main .book__title { padding-top: 6px; }
  .book__small { font-size: 19px; letter-spacing: .5px; text-transform: uppercase; }
  .book__big { font-family: "Alfa Slab One", Georgia, serif; color: var(--sky); font-size: 40px; margin: 4px 0; text-transform: uppercase; }
  .book__tag { display: inline-block; margin-top: 8px; padding: 2px 10px; background: var(--royal);
    font-family: "Alfa Slab One", Georgia, serif; font-size: 40px; color: var(--white); text-transform: uppercase; }
  .book--side .book__small { font-size: 13px; }
  .book--side .book__big { font-size: 28px; }
  .book--side .book__tag { font-size: 28px; }

  .cta { position: absolute; left: 0; right: 0; top: 735px; text-align: center;
    font-family: "Alfa Slab One", Georgia, serif; font-size: 52px; color: var(--yellow); text-transform: uppercase; }
</style>
</head>
<body>
  <main class="ad">
    <div class="ad__backdrop" role="img" aria-label="Dark, blurred close-up photograph used as background texture"></div>

    <svg class="ad__shapes" viewBox="0 0 860 832" aria-hidden="true">
      <path d="M0 360 C120 375 200 395 260 430 L0 420 Z" fill="var(--royal)"/>
      <path d="M0 380 C110 390 200 410 250 440 C180 415 100 405 0 405 Z" fill="var(--sky)"/>
      <path d="M860 268 C760 300 690 330 640 360 C720 335 790 320 860 312 Z" fill="var(--sky)"/>
      <path d="M860 310 C780 330 720 350 670 372 C740 360 800 352 860 350 Z" fill="var(--steel)"/>
      <path d="M860 338 L860 520 C790 440 720 400 650 380 C730 360 800 350 860 338 Z" fill="var(--royal)" opacity=".55"/>
      <path d="M0 610 C170 700 380 700 560 690 C690 682 790 700 860 740 L860 832 L0 832 Z" fill="var(--royal)"/>
      <path d="M0 745 C70 705 150 690 220 685 C140 710 70 740 30 790 Z" fill="var(--sky)"/>
      <path d="M0 700 C50 690 110 688 170 690 C100 700 40 720 0 745 Z" fill="var(--sky)"/>
      <path d="M520 832 C620 800 740 800 860 820 L860 832 Z" fill="var(--navy)"/>
    </svg>

    <h1 class="headline">
      <span class="headline__top">Making Sense of an</span>
      <span class="headline__bottom">Accident Claim</span>
    </h1>

    <div class="book book--side book--left">
      <div class="book__photo" role="img" aria-label="Cover photo of an injured man sitting on a gym floor holding his ankle"></div>
      <div class="book__title"><div class="book__small">Making Sense of</div><div class="book__big">An Accident</div><span class="book__tag">Claim</span></div>
    </div>
    <div class="book book--side book--right">
      <div class="book__photo" role="img" aria-label="Cover photo of an injured man sitting on a gym floor holding his ankle"></div>
      <div class="book__title"><div class="book__small">Making Sense of</div><div class="book__big">An Accident</div><span class="book__tag">Claim</span></div>
    </div>
    <div class="book book--main">
      <div class="book__photo" role="img" aria-label="Cover photo of an injured man sitting on a gym floor holding his ankle"></div>
      <div class="book__title"><div class="book__small">Making Sense of</div><div class="book__big">An Accident</div><span class="book__tag">Claim</span></div>
    </div>

    <p class="cta">Buy Now!</p>
  </main>
</body>
</html>
```